Thistlewood Candles, Hand-poured scented soy candles

Create a logo and label design to use on my vintage country farmhouse style, all natural, hand poured soy candle jars and apothecaries. Candles will be labeled in 4 different sizes so design must be adaptable, clean, simple, telegraphic and invoke interest in the product. Think Black lettering on white or black on kraft brown. Thistlewood is the area code for New Hampshire where we make them. The labels will need a prominent area for the scent of the candle to be listed that the eyes are drawn to. Primitive country in design? Use of state attractions? Jars are a square mason style 8 ounce and 16 ounce. Tarts are a clamshell. Lids are a 70-400 series 2.5" label area. Candles are white in a clear glass jar, black lids. There will be label design sizes of 3"x 2.5" 2.5" round, 1.5"x2.5"

Target Market(s)

primitive country, farmhouse, vintage, general home decor

Contact Information for Business Card

Thistlewood Candles, all natural soy candles, hand-poured in New Hampshire, logo, phone, address. Possibly match the main label.

Logo Text

Thistlewood Candles, all natural soy candles, hand-poured in New Hampshire, area for scent description and size of container.

Font styles to use
Serif
Script

Colors

Designer to choose colors to be used in the design.

Requirements
Must have
• simple and clean, country farmhouse with a bit of vintage thrown in. possibly multiple fonts to distinguish info from scent name
Nice to have
• at this time I am open to suggestions
• Prefer scent names or brand name in an older script?
• older copperplate/Spencerian?
Should not have
• cluttered, busy, too modern, multiple colors

```html
<!DOCTYPE html>
<html lang="en">
<head>
<meta charset="utf-8">
<title>Thistlewood Candles – Potpourri Label</title>
<link rel="stylesheet" href="https://fonts.googleapis.com/css2?family=IM+Fell+English&family=Libre+Baskerville:wght@400;700&family=Pinyon+Script&display=swap">
<style>
  :root {
    --page: #ffffff;
    --rim: #2b2118;
    --ink: #2a1c12;
    --copper-light: #e7a877;
    --copper-mid: #d08c5a;
    --copper-deep: #b26d3f;
    --band-dark: #2e2318;
    --band-edge: #5a4431;
    --band-text: #eab488;
  }
  html, body {
    margin: 0;
    width: 1200px;
    height: 1199px;
    overflow: hidden;
    background: var(--page);
  }
  .label {
    position: absolute;
    left: 50px;
    top: 50px;
    width: 1100px;
    height: 1100px;
  }
  .brand-name {
    font-family: "IM Fell English", serif;
    font-size: 52px;
    fill: var(--ink);
  }
  .brand-sub {
    font-family: "Libre Baskerville", serif;
    font-weight: 700;
    font-size: 22px;
    fill: var(--ink);
  }
  .scent-name {
    font-family: "Pinyon Script", cursive;
    font-size: 92px;
    fill: var(--ink);
  }
  .band-text {
    font-family: "Libre Baskerville", serif;
    font-weight: 700;
    font-size: 23px;
    fill: var(--band-text);
  }
  .scent-notes {
    font-family: "Libre Baskerville", serif;
    font-weight: 700;
    font-size: 11.5px;
    fill: var(--ink);
  }
  .origin {
    font-family: "IM Fell English", serif;
    font-size: 22px;
    fill: var(--ink);
  }
</style>
</head>
<body>
<svg class="label" viewBox="352 383 570 570" xmlns="http://www.w3.org/2000/svg">
  <defs>
    <radialGradient id="copperFill" cx="45%" cy="40%" r="65%">
      <stop offset="0" stop-color="var(--copper-light)"/>
      <stop offset="0.6" stop-color="var(--copper-mid)"/>
      <stop offset="1" stop-color="var(--copper-deep)"/>
    </radialGradient>
    <linearGradient id="bandFill" x1="0" y1="0" x2="0" y2="1">
      <stop offset="0" stop-color="var(--band-edge)"/>
      <stop offset="0.5" stop-color="var(--band-dark)"/>
      <stop offset="1" stop-color="var(--band-edge)"/>
    </linearGradient>
    <clipPath id="faceClip">
      <circle cx="637" cy="668" r="270"/>
    </clipPath>
    <path id="originArc" d="M 410 700 A 232 232 0 0 0 864 700"/>
  </defs>

  <circle class="rim" cx="637" cy="668" r="285" fill="var(--rim)"/>
  <circle class="face" cx="637" cy="668" r="270" fill="url(#copperFill)"/>
  <circle class="inner-rule" cx="637" cy="668" r="262" fill="none" stroke="var(--ink)" stroke-width="1.5"/>

  <text class="brand-name" x="637" y="490" text-anchor="middle">Thistlewood</text>
  <text class="brand-sub" x="637" y="522" text-anchor="middle">Candles</text>

  <text class="scent-name" x="637" y="650" text-anchor="middle">Potpourri</text>

  <g clip-path="url(#faceClip)">
    <rect class="band" x="352" y="697" width="570" height="46" fill="url(#bandFill)"/>
  </g>
  <text class="band-text" x="637" y="729" text-anchor="middle">All Natural Soy Candles</text>

  <g class="scent-notes" text-anchor="middle">
    <text x="637" y="766">Lorem ipsum dolor sit amet, consectetur</text>
    <text x="637" y="781">adipiscing elit, sed do eiusmod tempor</text>
    <text x="637" y="796">incididunt ut labore et dolore magna aliqua.</text>
    <text x="637" y="811">Ut enim ad minim veniam, quis nostrud</text>
    <text x="637" y="826">exercitation ullamco laboris .</text>
  </g>

  <text class="origin"><textPath href="#originArc" startOffset="50%" text-anchor="middle">Hand-poured in New Hampshire</textPath></text>
</svg>
</body>
</html>
```